Thimble Nook web site

I have been running an online business for 6 years.
www.thimblenook.com.au I specialise in ribbons, buttons and unique craft materials. I sell online to individuals and shops with seperate retail and wholesale sites. The web page I'd like redesigned is my retail site.

It needs a clean, fresh look. I've recently had a new logo designed (thanks pixel harbour!) and want the web site to incorporate the new design and colour scheme of black and white. (new logo attached as a file)

I no longer want the page with the large image www.thimblenook.com.au I want to have the first page as the retail shop homepage.
http://www.thimblenook.com.au/index.php so this page needs to have all the links

I want to the look to be fresh, modern and clear. It needs to be quick to load.

Notes from my IT guru: They need to know that the following tend to remain static with just the content section changing on each page; Header Left column (but different in the cart) right column (if required) footer
Updates

Thanks for your designs. 1/3 of my users use mobile devices so please take that into consideration. I would like the logo to be incorporated into the design and be a prominent feature (most have just used it as a tiny image in the top left corner. I would like it to be larger and more prominent.  thanks                                   

Thanks to all the designers who have submitted. Can you please add  'Boutique craft supplies' near the logo. That is my tag line. Thanks

Target Market(s)

Crafty females of all ages

Industry/Entity Type

Business

Requirements
Must have
• links to;
blog
gallery
chatterloop
snapboardly
wholesale
space for an image which I change approx every 2 weeks
about Thimble Nook
contact
privacy policy
terms and conditions
newsletter sign up
shipping info
product search
Nice to have
• I am not sure if I want product images on the homepage? I have attached a few images.
Should not have
• not too much colour - I hate the green border I have now

```html
<!DOCTYPE html>
<html lang="en">
<head>
<meta charset="utf-8">
<title>Thimble Nook – Boutique craft supplies</title>
<link rel="stylesheet" href="https://fonts.googleapis.com/css2?family=Source+Sans+3:wght@300;400;600&display=swap">
<style>
:root{
  --ink:#1a1a1a;
  --text:#2b2b2b;
  --white:#ffffff;
  --line:#c9c9c9;
  --frame:#d2d2d2;
  --nav-active:#5a5a5a;
  --price:#e4511c;
  --bar-top:#2a2a2a;
  --bar-bottom:#050505;
  --footer:#e9e9e9;
}
*{box-sizing:border-box;margin:0;padding:0}
html,body{width:1096px;height:1200px;overflow:hidden}
body{position:relative;font-family:"Source Sans 3",sans-serif;color:var(--text);
  background:linear-gradient(90deg,#ececec 0%,#fafafa 50%,#ececec 100%)}
a{color:inherit;text-decoration:none}
.abs{position:absolute}

/* header */
.brand{left:148px;top:14px;display:flex;align-items:center;gap:14px}
.brand-dot{width:76px;height:76px;border-radius:50%;background:var(--ink);flex:none}
.brand-name{font-size:38px;font-weight:400;color:var(--ink);line-height:40px;letter-spacing:.5px}
.brand-tagline{font-size:15px;font-weight:300;color:#555;letter-spacing:1.5px;margin-top:2px}
.util-btn{top:7px;height:21px;border:1px solid var(--line);background:var(--white);font-size:11px;
  display:flex;align-items:center;justify-content:center;gap:6px;color:var(--ink)}
.phone{left:711px;top:49px;display:flex;align-items:center;gap:8px;font-size:18px;color:var(--ink)}
.phone-icon{width:19px;height:21px;border:1px solid var(--line);background:var(--white);display:flex;align-items:center;justify-content:center}
.search{left:853px;top:47px;width:101px;height:26px;border:1px solid var(--line);background:var(--white);
  display:flex;align-items:center;gap:6px;padding-left:7px;font-size:10px;color:var(--ink)}

/* navigation */
.nav{left:0;top:105px;width:1096px;height:30px;background:linear-gradient(var(--bar-top),var(--bar-bottom))}
.nav-item{top:0;height:30px;display:flex;align-items:center;justify-content:center;color:var(--white);font-size:12px}
.nav-item.is-active{background:var(--nav-active)}
.nav-sep{top:0;width:1px;height:30px;background:#555}

/* slider */
.slider{left:149px;top:143px;width:808px;height:348px;border:1px solid var(--frame);background:var(--white);padding:3px}
.slide-photo{width:100%;height:100%;background:linear-gradient(170deg,#e6e2ee 0%,#c8b6e6 30%,#f0c6d6 50%,#f3e58c 70%,#d9ecb8 85%,#e8e8e8 100%)}
.slide-arrow{top:294px;width:48px;height:48px;border-radius:50%;background:#5b5b5b;display:flex;align-items:center;justify-content:center}
.slide-caption{left:153px;top:464px;width:802px;height:25px;background:rgba(110,110,110,.9);color:var(--white);font-size:12.5px;padding:4px 8px}

/* products */
.section-title{font-weight:300;color:var(--ink)}
.latest-title{left:0;width:1096px;top:506px;text-align:center;font-size:24px}
.products{left:150px;top:541px;width:807px;height:197px;border:1px solid var(--frame);background:var(--white)}
.product-img{top:553px;width:186px;height:105px;border:1px solid var(--frame);padding:3px;background:var(--white)}
.product-img span{display:block;width:100%;height:100%}
.product-name{top:666px;font-size:16.5px;font-weight:300;color:var(--ink)}
.product-price{top:687px;font-size:14px;color:var(--price)}
.product-sep{top:670px;width:1px;height:54px;background:var(--line)}
.btn{background:linear-gradient(#3a3a3a,#060606);color:var(--white);font-size:10px;display:flex;align-items:center;justify-content:center;border-radius:2px}
.cart-btn{top:710px;width:73px;height:18px}

/* welcome */
.welcome-title{left:150px;top:758px;font-size:23px}
.welcome-text{left:152px;top:794px;width:525px;font-size:11.2px;line-height:17px;text-align:justify}
.welcome-text p+p{margin-top:10px}
.panel{top:933px;width:258px;height:120px;border:1px solid #d8d8d8;background:linear-gradient(135deg,#f7f7f7,#ececec)}
.panel-title{font-size:19px;font-weight:300;color:var(--ink)}
.panel-text{font-size:10.8px;line-height:17px}
.email-field{left:17px;top:64px;width:223px;height:27px;border:1px solid #cfcfcf;background:var(--white);font-size:9.5px;padding:7px 9px;color:#444}

/* sale */
.sale-title{left:717px;top:758px;font-size:23px}
.sale-img{left:718px;width:70px;height:66px;border:1px solid var(--frame);padding:3px;background:var(--white)}
.sale-img span{display:block;width:100%;height:100%;background:linear-gradient(135deg,#f3f3f3,#bdbdbd)}
.sale-name{left:799px;width:170px;font-size:14px;line-height:19px;color:var(--ink)}
.sale-price{font-size:14px;color:var(--price);margin-top:3px}
.sale-rule{left:718px;width:240px;border-top:1px dotted #999}

/* footer */
.footer{left:0;top:1069px;width:1096px;height:131px;background:var(--footer)}
.follow{top:1082px;width:1096px;left:0;text-align:center;font-size:11px;color:var(--ink)}
.social{top:1100px;left:0;width:1096px;display:flex;justify-content:center;gap:22px;font-size:11px;color:var(--ink)}
.social a{display:flex;align-items:center;gap:6px}
.social-mark{width:14px;height:14px;border-radius:2px;background:#333}
.footer-rule{left:153px;top:1125px;width:817px;height:1px;background:#cdcdcd}
.footer-links{left:0;width:1096px;text-align:center;font-size:11px;color:var(--ink);word-spacing:2px}
.copyright{top:1174px;left:0;width:1096px;text-align:center;font-size:11px;color:var(--ink)}
</style>
</head>
<body>

<header>
  <div class="abs brand">
    <span class="brand-dot"></span>
    <div>
      <div class="brand-name">Thimble Nook</div>
      <div class="brand-tagline">Boutique craft supplies</div>
    </div>
  </div>
  <a class="abs util-btn" style="left:702px;width:51px">Register</a>
  <a class="abs util-btn" style="left:760px;width:39px">Login</a>
  <a class="abs util-btn" style="left:805px;width:148px">
    <svg width="15" height="11" viewBox="0 0 15 11"><path d="M0 1h3l2 7h8l2-5H4" fill="none" stroke="#222" stroke-width="1.4"/><circle cx="6" cy="10" r="1" fill="#222"/><circle cx="12" cy="10" r="1" fill="#222"/></svg>
    Shopping Cart (0) items</a>
  <div class="abs phone">
    <span class="phone-icon"><svg width="11" height="13" viewBox="0 0 11 13"><path d="M2 0h2l1 3-2 1c1 2 2 4 4 5l1-2 3 1v2c0 1-1 2-2 2C4 12 0 7 0 2 0 1 1 0 2 0z" fill="#222"/></svg></span>
    414.555.0182
  </div>
  <div class="abs search">
    <svg width="12" height="12" viewBox="0 0 12 12"><circle cx="5" cy="5" r="3.5" fill="none" stroke="#444" stroke-width="1.5"/><path d="M7.5 7.5l3.5 3.5" stroke="#444" stroke-width="2"/></svg>
    Search
  </div>
</header>

<nav class="abs nav">
  <a class="abs nav-item is-active" style="left:170px;width:72px">Home</a>
  <span class="abs nav-sep" style="left:258px"></span>
  <a class="abs nav-item" style="left:258px;width:109px">About Us</a>
  <span class="abs nav-sep" style="left:367px"></span>
  <a class="abs nav-item" style="left:367px;width:99px">Our Products</a>
  <span class="abs nav-sep" style="left:466px"></span>
  <a class="abs nav-item" style="left:466px;width:108px">Shop</a>
  <span class="abs nav-sep" style="left:574px"></span>
  <a class="abs nav-item" style="left:574px;width:99px">Wholesale</a>
  <span class="abs nav-sep" style="left:673px"></span>
  <a class="abs nav-item" style="left:673px;width:97px">Gallery</a>
  <span class="abs nav-sep" style="left:770px"></span>
  <a class="abs nav-item" style="left:770px;width:99px">Blog</a>
  <span class="abs nav-sep" style="left:869px"></span>
  <a class="abs nav-item" style="left:869px;width:99px">Contact us</a>
</nav>

<section>
  <div class="abs slider"><div class="slide-photo" role="img" aria-label="Photo of coiled pastel gingham ribbons in purple, pink, yellow, green and blue"></div></div>
  <span class="abs slide-arrow" style="left:176px"><svg width="16" height="22" viewBox="0 0 16 22"><path d="M12 2L3 11l9 9" fill="none" stroke="#fff" stroke-width="3.5"/></svg></span>
  <span class="abs slide-arrow" style="left:884px"><svg width="16" height="22" viewBox="0 0 16 22"><path d="M4 2l9 9-9 9" fill="none" stroke="#fff" stroke-width="3.5"/></svg></span>
  <div class="abs slide-caption">Lorem Ipsum is simply dummy text of the printing and typesetting industry. Lorem Ipsum</div>
</section>

<section>
  <h2 class="abs section-title latest-title">Latest Products</h2>
  <div class="abs products"></div>

  <div class="abs product-img" style="left:160px"><span role="img" aria-label="Photo of stacked washi tape rolls" style="background:linear-gradient(#dcdcd6,#8a9a55 35%,#e9c23c 65%,#d86a3c)"></span></div>
  <div class="abs product-name" style="left:161px">Washi tape</div>
  <div class="abs product-price" style="left:161px">$3.50</div>
  <a class="abs btn cart-btn" style="left:162px">Add to Cart</a>
  <span class="abs product-sep" style="left:345px"></span>

  <div class="abs product-img" style="left:362px"><span role="img" aria-label="Photo of satin ribbon pom pom flowers in red, pink and green" style="background:linear-gradient(90deg,#a52a38,#c99aa0 50%,#a8c88a)"></span></div>
  <div class="abs product-name" style="left:361px">Pom pom large</div>
  <div class="abs product-price" style="left:362px">$3.50</div>
  <a class="abs btn cart-btn" style="left:363px">Add to Cart</a>
  <span class="abs product-sep" style="left:547px"></span>

  <div class="abs product-img" style="left:564px"><span role="img" aria-label="Photo of striped ribbon rolls in black, red, green, yellow and blue" style="background:linear-gradient(90deg,#3a3a3a,#d55a60 25%,#b6d06a 50%,#e9cf78 70%,#86c4d6)"></span></div>
  <div class="abs product-name" style="left:565px">Bat ribbon</div>
  <div class="abs product-price" style="left:566px">$450</div>
  <a class="abs btn cart-btn" style="left:566px">Add to Cart</a>
  <span class="abs product-sep" style="left:749px"></span>

  <div class="abs product-img" style="left:764px"><span role="img" aria-label="Photo of patterned ribbon club assortment" style="background:linear-gradient(90deg,#9ccc70,#f0a8c0 40%,#e88ab0 60%,#9ccc70)"></span></div>
  <div class="abs product-name" style="left:764px">Ribbon Club</div>
  <div class="abs product-price" style="left:763px">$15.50</div>
  <a class="abs btn cart-btn" style="left:765px">Add to Cart</a>
  <span class="abs product-sep" style="left:949px"></span>
</section>

<section>
  <h2 class="abs section-title welcome-title">Welcome!</h2>
  <div class="abs welcome-text">
    <p>Thimble Nook is a retail and wholesale business specialising in unique ribbons and embellishment. Company owner Maren has sourced an amazing range of ribbons and embellishments suitable for a diverse range of crafts including scrapbooking, card making, patchwork and sewing.</p>
    <p>As a direct importer, Maren consistently manages to introduce new products to the Australian market. This results in excellent value for money, without compromising on quality.</p>
  </div>
  <a class="abs btn" style="left:153px;top:897px;width:73px;height:18px">Read More</a>

  <div class="abs panel" style="left:153px">
    <div class="abs panel-title" style="left:15px;top:11px">Mailing List</div>
    <div class="abs panel-text" style="left:17px;top:42px">Subscribe to our mailing list below:</div>
    <div class="abs email-field">Enter the Email id</div>
    <a class="abs btn" style="left:178px;top:98px;width:62px;height:20px">SUBSCRIBE</a>
  </div>

  <div class="abs panel" style="left:428px">
    <div class="abs panel-title" style="left:15px;top:10px">Wholesale</div>
    <div class="abs panel-text" style="left:16px;top:43px;width:170px">If you wish to apply for a wholesale account with Thimble Nook, please download and complete ...</div>
    <a class="abs btn" style="left:16px;top:96px;width:73px;height:18px">Read More</a>
    <svg class="abs" style="left:200px;top:57px" width="44" height="50" viewBox="0 0 44 50"><rect x="2" y="16" width="26" height="20" rx="3" fill="#444"/><rect x="9" y="10" width="12" height="7" fill="none" stroke="#444" stroke-width="2.5"/><path d="M2 40h32V10l8-6" fill="none" stroke="#444" stroke-width="3"/><circle cx="7" cy="45" r="4" fill="#444"/><circle cx="29" cy="45" r="4" fill="#444"/></svg>
  </div>
</section>

<aside>
  <h2 class="abs section-title sale-title">Sale Items</h2>

  <div class="abs sale-img" style="top:799px"><span role="img" aria-label="Product photo of clear stamp set with bracket shapes"></span></div>
  <div class="abs sale-name" style="top:795px">Inkwell Lane clear stamp - brackets<div class="sale-price">Save $18.95</div></div>
  <div class="abs sale-rule" style="top:877px"></div>

  <div class="abs sale-img" style="top:889px"><span role="img" aria-label="Product photo of clear stamp set with flourishes"></span></div>
  <div class="abs sale-name" style="top:887px">Inkwell Lane clear stamp - flourishes<div class="sale-price">Save $16.95</div></div>
  <div class="abs sale-rule" style="top:967px"></div>

  <div class="abs sale-img" style="top:978px"><span role="img" aria-label="Product photo of clear stamp set with floral expressions"></span></div>
  <div class="abs sale-name" style="top:975px">Inkwell Lane clear stamp - floral expressions<div class="sale-price">Save $12.00</div></div>
</aside>

<footer>
  <div class="abs footer"></div>
  <div class="abs follow">Follow us On</div>
  <div class="abs social">
    <a><span class="social-mark"></span>chatterloop</a>
    <a><span class="social-mark"></span>snapboardly</a>
  </div>
  <div class="abs footer-rule"></div>
  <div class="abs footer-links" style="top:1134px">Home &nbsp;|&nbsp; About Us &nbsp;|&nbsp; Services &nbsp;|&nbsp; Shop &nbsp;|&nbsp; Wholesale &nbsp;|&nbsp; Gallery &nbsp;|&nbsp; Blog &nbsp;|&nbsp; Contact us</div>
  <div class="abs footer-links" style="top:1153px">Privacy Policy &nbsp;|&nbsp; Terms and Conditions &nbsp;|&nbsp; Shipping Info</div>
  <div class="abs copyright">Copyrights @ 2013 All Rights Reserved</div>
</footer>

</body>
</html>
```